Roof Plumbing Company needs simple, modern business card using the attached logo and below details:

Glen Marwick
Kestrel Roofing Pty Ltd
ABN: 58 217 934 062
Phone: 0417 286 503
Email: kestrelroofing@mailvista.com
Website: kestrelroofing.com.au

For all of your metal roof plumbing requirements contact Kestrel Roofing for an obligation free quote - no job too big or to small!

Industry/Entity Type

Business

Contact Information for Business Card

Glen Marwick
Kestrel Roofing Pty Ltd
ABN 58 217 934 062
0417 286 503
kestrelroofing@mailvista.com
kestrelroofing.com.au

Requirements
Must have
• Bright eye catching design, professional look

```html
<!DOCTYPE html>
<html lang="en">
<head>
<meta charset="utf-8">
<title>Kestrel Roofing Pty Ltd — Business Card</title>
<link rel="stylesheet" href="https://fonts.googleapis.com/css2?family=Montserrat:wght@600&family=Open+Sans:wght@400&display=swap">
<style>
  :root {
    --backdrop: #aeacad;
    --card: #fbfbfb;
    --brand-red: #d42a2a;
    --brand-red-dark: #a81c1c;
    --slate: #4a4a4c;
    --text: #4a4a4c;
  }
  html, body {
    margin: 0;
    width: 1200px;
    height: 1200px;
    overflow: hidden;
    background: var(--backdrop);
  }
  .card {
    position: absolute;
    width: 712px;
    height: 418px;
    background: var(--card);
    border-radius: 24px;
    overflow: hidden;
  }
  .card--front { left: 238px; top: 118px; }
  .card--back  { left: 230px; top: 645px; }

  .wordmark {
    position: absolute;
    margin: 0;
    font-family: "Montserrat", sans-serif;
    font-weight: 600;
    color: var(--brand-red);
    line-height: 1.1;
    white-space: nowrap;
  }
  .card--front .wordmark {
    left: 0; right: 0;
    top: 118px;
    text-align: center;
    font-size: 66px;
    letter-spacing: 0.5px;
  }
  .card--back .wordmark {
    left: 40px;
    top: 72px;
    font-size: 40px;
  }

  .person {
    position: absolute;
    left: 404px;
    top: 160px;
  }
  .person__name {
    margin: 0;
    font-family: "Montserrat", sans-serif;
    font-weight: 600;
    font-size: 27px;
    color: var(--brand-red);
    letter-spacing: 0.3px;
  }
  .person__role {
    margin: 6px 0 0;
    font-family: "Open Sans", sans-serif;
    font-size: 16px;
    color: var(--text);
  }

  .contact {
    position: absolute;
    left: 404px;
    top: 250px;
    margin: 0;
    padding: 0;
    list-style: none;
    font-family: "Open Sans", sans-serif;
    font-size: 18px;
    color: var(--text);
  }
  .contact__item {
    display: flex;
    align-items: center;
    height: 25px;
  }
  .contact__icon {
    width: 16px;
    height: 16px;
    margin-right: 18px;
    fill: var(--brand-red);
  }
  .contact__item--abn { margin-top: 5px; }

  .card__band {
    position: absolute;
    left: 0;
    bottom: 0;
    width: 712px;
    height: 24px;
  }
</style>
</head>
<body>

<section class="card card--front" aria-label="Card front">
  <h1 class="wordmark">Kestrel Roofing<br>Pty Ltd</h1>
</section>

<section class="card card--back" aria-label="Card back">
  <p class="wordmark">Kestrel Roofing<br>Pty Ltd</p>

  <div class="person">
    <p class="person__name">Glen Marwick</p>
    <p class="person__role">Director</p>
  </div>

  <ul class="contact">
    <li class="contact__item">
      <svg class="contact__icon" viewBox="0 0 16 16" aria-hidden="true">
        <path d="M2 5c0-2 3-3 6-3s6 1 6 3v1h-3V5H5v1H2z"/>
        <rect x="3" y="8" width="10" height="6" rx="1"/>
      </svg>
      0417 286 503
    </li>
    <li class="contact__item">
      <svg class="contact__icon" viewBox="0 0 16 16" aria-hidden="true">
        <circle cx="8" cy="8" r="7" fill="none" stroke="#d42a2a" stroke-width="1.6"/>
        <ellipse cx="8" cy="8" rx="3" ry="7" fill="none" stroke="#d42a2a" stroke-width="1.4"/>
        <path d="M1 8h14" stroke="#d42a2a" stroke-width="1.4"/>
      </svg>
      kestrelroofing.com.au
    </li>
    <li class="contact__item">
      <svg class="contact__icon" viewBox="0 0 16 16" aria-hidden="true">
        <rect x="1" y="3" width="14" height="10"/>
        <path d="M1 3l7 6 7-6" fill="none" stroke="#fbfbfb" stroke-width="1.3"/>
      </svg>
      kestrelroofing@mailvista.com
    </li>
    <li class="contact__item contact__item--abn">ABN 58 217 934 062</li>
  </ul>

  <svg class="card__band" viewBox="0 0 712 24" preserveAspectRatio="none" aria-hidden="true">
    <defs>
      <linearGradient id="bandRed" x1="0" x2="1" y1="0" y2="0">
        <stop offset="0" stop-color="#a81c1c"/>
        <stop offset="0.5" stop-color="#d42a2a"/>
        <stop offset="1" stop-color="#e03030"/>
      </linearGradient>
    </defs>
    <polygon points="0,2 500,2 478,24 0,24" fill="url(#bandRed)"/>
    <polygon points="506,0 712,0 712,24 484,24" fill="#4a4a4c"/>
  </svg>
</section>

</body>
</html>
```